A modern and fresh looking church website

St Maren’s is looking for a new site design for their church. The church is a part of a group of the ‘Calverin Church’ Australia and needs to kind of tie into their branding within reason.
This means, we would need to use the logo colours (Blue, Gold, Red) throughout the website and the design needs to be fresh, modern, clean, and mobile-friendly. The front page must have the following as features:
• Sermons (Podcasts and Videos)
• Events
• Venue Hire (Weddings)
The website will be mainly information-based and will have a few forms. From our recent engagement with the church, I did draft up a mock-up design for them and even it looks better than their current site, it’s not giving a ‘stand out impression’ and has that out of date look.
The inner pages will be based off the front-page design so we will take care of that, we are just looking for a front-page design that is unique and has the wow factor.
The website will be coded by our in-house development team and will be coded in a WordPress format using Elementor pro.
We are looking for a couple of designers to design 1-3 mock-ups by taking our current draft and putting their spin to it.
Hi,
Due to Christmas and the client was on leave, the design selection has been delayed. It was not ideal as I knew this would happen.
I made contact with the client and just been told that the client is leaving the church and a handover is happening for the new staff member. The new staff member will present all designs to the board for selection. This is due to be completed by the first week of February 2021.
We thanks for your patients as this was not expected and we seeing if we can hurry this process up.

```html
<!DOCTYPE html>
<html lang="en">
<head>
<meta charset="utf-8">
<title>St Maren’s Calverin Church Perth</title>
<link href="https://fonts.googleapis.com/css2?family=IBM+Plex+Sans:wght@400;500;600;700&display=swap" rel="stylesheet">
<style>
:root{
  --blue:#0d3d8c;
  --blue-band:#1456b3;
  --navy:#1a2a5a;
  --gold:#b98a3c;
  --orange:#f7943a;
  --red:#e0232b;
  --ink:#2b2b2b;
  --light:#f4f1f1;
  --footer:#1b1b1b;
  --white:#fff;
}
*{margin:0;padding:0;box-sizing:border-box}
html,body{width:1200px;height:2502px;overflow:hidden}
body{font-family:"IBM Plex Sans",Arial,sans-serif;color:var(--ink);background:var(--white);position:relative}
.abs{position:absolute}
/* header */
.brand{left:132px;top:24px;display:flex;align-items:center;gap:10px}
.brand-mark{width:52px;height:52px;border-radius:50%;background:var(--blue)}
.brand-name{color:var(--blue);font-weight:700;font-size:30px;line-height:1;letter-spacing:.5px}
.brand-name small{display:block;font-size:12.5px;letter-spacing:.8px;margin-top:5px}
.follow{left:748px;top:23px;display:flex;align-items:center;gap:6px;font-size:11px;font-weight:600;color:var(--navy)}
.dot{width:27px;height:27px;border-radius:50%;display:flex;align-items:center;justify-content:center}
.call{left:918px;top:21px;display:flex;align-items:center;gap:9px}
.call .lbl{font-size:10.5px;font-weight:600;color:var(--navy);line-height:1}
.call .num{font-size:18px;font-weight:500;color:var(--blue);line-height:1.1}
.nav{left:510px;top:67px;display:flex;gap:26px;font-size:12.5px;font-weight:700;color:var(--blue)}
.nav .on{color:var(--red);text-decoration:underline;text-underline-offset:4px}
/* hero */
.hero{left:0;top:101px;width:1200px;height:549px;background:linear-gradient(120deg,#6a4a3a 0%,#8a5a48 35%,#a8866e 55%,#5a3a30 100%)}
.hero-kicker{left:132px;top:423px;color:#fff;font-weight:700;font-size:20px}
.hero-title{left:131px;top:444px;color:#fff;font-weight:700;font-size:54px;letter-spacing:1px}
.btn{background:var(--orange);color:#fff;font-weight:700;text-transform:uppercase;display:inline-flex;align-items:center;justify-content:center}
.hero-btn{left:132px;top:523px;width:125px;height:40px;font-size:15.5px}
.dots{left:562px;top:608px;display:flex;gap:9px;align-items:center}
.dots i{width:6px;height:6px;border-radius:50%;background:#fff;display:block}
.dots i.on{width:11px;height:11px;border:2px solid #fff;background:var(--red)}
/* section titles */
.sec-title{width:1200px;left:0;text-align:center;font-weight:700;font-size:22px}
.sec-title::after{content:"";display:block;width:44px;height:2px;margin:9px auto 0;background:var(--gold)}
/* sermons */
.sermon{width:300px;height:328px;border:1px solid #cfcfcf;top:759px;background:#fff}
.sermon .ph{height:222px;width:100%}
.sermon .meta{text-align:center;padding:22px 24px 0;font-size:13px;line-height:19px;color:#333}
.sermon .meta b{display:block;color:var(--blue);font-weight:700;font-size:13px}
.player{position:absolute;left:27px;top:192px;width:246px;height:30px;background:#111;display:flex;align-items:center;gap:10px;padding:0 14px;color:#fff;font-size:8px}
.player .bar{flex:1;height:6px;background:#555}
.player .vol{width:40px;height:4px;background:#fff}
.play{position:absolute;left:144px;top:82px;width:64px;height:64px;border:3px solid #fff;border-radius:50%;background:rgba(0,0,0,.35)}
.arrow{top:906px}
/* events */
.events{left:0;top:1137px;width:1200px;height:507px;background:var(--blue-band)}
.event{top:1249px;width:222px;height:349px;background:#fff}
.event .ph{height:155px}
.event .body{padding:20px 22px 0}
.event h3{font-size:13px;line-height:17.5px;font-weight:700;color:var(--blue);text-transform:uppercase;min-height:35px}
.event p{font-size:10.8px;line-height:14.5px;color:#333;margin-top:13px;min-height:60px}
.event .btn{width:81px;height:25px;font-size:9.5px;margin-top:6px}
/* venue */
.venue{left:0;top:1644px;width:1200px;height:519px;background:var(--light)}
.venue-title{left:668px;top:1699px;color:var(--blue);font-weight:700;font-size:23px}
.venue-title::after{content:"";display:block;width:47px;height:2px;background:var(--gold);margin-top:10px}
.venue-text{left:671px;top:1761px;width:410px;font-size:15.2px;line-height:21px;color:#333}
.venue-text p+p{margin-top:22px}
.venue-btn{left:672px;top:2063px;width:124px;height:40px;font-size:15.5px}
/* footer */
.footer{left:0;top:2163px;width:1200px;height:339px;background:var(--footer);color:#ddd}
.f-brand{left:130px;top:2263px;display:flex;align-items:center;gap:10px;opacity:.55}
.f-head{top:2207px;font-size:13px;font-weight:700;color:#fff;letter-spacing:.4px}
.f-menu{left:549px;top:2245px;font-size:11.5px;line-height:20px;color:#ddd}
.f-item{display:flex;gap:10px;align-items:flex-start;font-size:11.5px;line-height:16px;color:#ddd}
.f-ico{width:24px;height:24px;border-radius:50%;background:#fff;flex:none;display:flex;align-items:center;justify-content:center;margin-top:2px}
.rule{left:126px;top:2426px;width:933px;height:1px;background:#3a3a3a}
.copy{left:0;width:1200px;top:2461px;text-align:center;font-size:9.5px;color:#ccc}
</style>
</head>
<body>

<header>
  <div class="abs brand">
    <span class="brand-mark"></span>
    <span class="brand-name">ST MAREN’S<small>CALVERIN CHURCH PERTH</small></span>
  </div>
  <div class="abs follow">FOLLOW
    <span class="dot" style="background:#3b5bb5"></span>
    <span class="dot" style="background:#1da1f2"></span>
    <span class="dot" style="background:var(--navy)"></span>
  </div>
  <div class="abs call">
    <span class="dot" style="background:var(--navy)"><svg width="13" height="13" viewBox="0 0 24 24"><path fill="#fff" d="M6.6 10.8a15 15 0 006.6 6.6l2.2-2.2a1 1 0 011-.25 11.4 11.4 0 003.6.6 1 1 0 011 1V20a1 1 0 01-1 1A17 17 0 013 4a1 1 0 011-1h3.5a1 1 0 011 1c0 1.25.2 2.45.6 3.6a1 1 0 01-.25 1z"/></svg></span>
    <div><div class="lbl">CALL US</div><div class="num">800.555.0142</div></div>
  </div>
  <nav class="abs nav">
    <span class="on">HOME</span><span>SERMONS</span><span>ABOUT US</span><span>CHURCH LIFE</span><span>NEWS</span><span>WEDDINGS</span><span>CONTACTS</span>
  </nav>
</header>

<section>
  <div class="abs hero" role="img" aria-label="Photo of the congregation standing together inside the church beside the baptismal font"></div>
  <div class="abs hero-kicker">WELCOME TO</div>
  <div class="abs hero-title">WORSHIP</div>
  <span class="abs btn hero-btn">Read More</span>
  <div class="abs dots"><i></i><i></i><i class="on"></i><i></i><i></i></div>
</section>

<section>
  <h2 class="abs sec-title" style="top:686px;color:var(--blue)">SERMONS</h2>
  <svg class="abs arrow" style="left:60px" width="22" height="34" viewBox="0 0 22 34"><path d="M18 2L4 17l14 15" fill="none" stroke="#777" stroke-width="1.5"/></svg>
  <svg class="abs arrow" style="left:1110px" width="22" height="34" viewBox="0 0 22 34"><path d="M4 2l14 15L4 32" fill="none" stroke="#777" stroke-width="1.5"/></svg>

  <article class="abs sermon" style="left:133px">
    <div class="ph" style="position:relative;background:linear-gradient(180deg,#5b4a3e,#8a7a6a)" role="img" aria-label="Video still of the pastor reading at the altar">
      <span class="play"></span>
    </div>
    <div class="meta"><b>29 NOVEMBER, PREPARING FOR THE LORD’S COMING – A REALITY CHECK, MARK 13:32-37</b></div>
  </article>
  <article class="abs sermon" style="left:451px">
    <div class="ph" style="position:relative;background:linear-gradient(180deg,#c9b890,#6f6450)" role="img" aria-label="Photo of an ornate gothic church interior">
      <div class="player"><span>▶</span><span>00:00</span><span class="bar"></span><span>00:00</span><span class="vol"></span></div>
    </div>
    <div class="meta">22 March – Pastor Tomas Vell<b style="margin-top:6px">PSALM 23 &amp; PSALM 46: A MIGHTY FORTRESS IS OUR GOD</b></div>
  </article>
  <article class="abs sermon" style="left:770px">
    <div class="ph" style="position:relative;background:linear-gradient(180deg,#1e1a22,#3a4f6a 55%,#1a1a1a)" role="img" aria-label="Photo of stained glass windows in a dark church">
      <div class="player"><span>▶</span><span>00:00</span><span class="bar"></span><span>00:00</span><span class="vol"></span></div>
    </div>
    <div class="meta">15 March – Pastor Ian Corrow<b style="margin-top:6px">JESUS AND THE<br>SAMARITAN WOMAN</b></div>
  </article>
</section>

<section>
  <div class="abs events"></div>
  <h2 class="abs sec-title" style="top:1177px;color:#fff">EVENTS</h2>
  <article class="abs event" style="left:132px">
    <div class="ph" style="background:linear-gradient(180deg,#7fb0e0,#2f5aa0 60%,#6a6a5a)" role="img" aria-label="Group of walkers in blue shirts"></div>
    <div class="body"><h3>Walk My Way – Rockingham – Saturday 27 April</h3>
    <p>What a success, thanks to Western Australian walkers and volunteers more than $20,000 was raised from the 25km walk.</p>
    <span class="btn">Read More</span></div>
  </article>
  <article class="abs event" style="left:370px">
    <div class="ph" style="background:linear-gradient(180deg,#1c2a5a,#4a4a52)" role="img" aria-label="Church building lit at dusk"></div>
    <div class="body"><h3>Donate to St Maren’s Calverin Church</h3>
    <p>We won’t be seeing a collection plate for a while, but it’s important to continue to support your congregation’s</p>
    <span class="btn">Read More</span></div>
  </article>
  <article class="abs event" style="left:608px">
    <div class="ph" style="background:linear-gradient(180deg,#2a2a2e,#6a3a3a)" role="img" aria-label="Carol singers performing in the courtyard at night"></div>
    <div class="body"><h3>Carols in the Courtyard 2019</h3>
    <p>Joy came to the city of Perth as once again we joined together in singing our favourite Christmas songs.</p>
    <span class="btn">Read More</span></div>
  </article>
  <article class="abs event" style="left:847px">
    <div class="ph" style="background:linear-gradient(180deg,#8a8878,#4a4a3a)" role="img" aria-label="Painting of a nativity scene inside a wreath"></div>
    <div class="body"><h3>Advent – Preparing for Christmas</h3>
    <p>Members of St Maren’s were asked to paint what the John 6 readings about Jesus as the Bread of Life meant to them.</p>
    <span class="btn">Read More</span></div>
  </article>
</section>

<section>
  <div class="abs venue"></div>
  <div class="abs" style="left:132px;top:1701px;width:481px;height:266px;background:linear-gradient(135deg,#6b4a32,#a88a6a 50%,#5a4a3a)" role="img" aria-label="Wedding couple beside a white limousine outside the church"></div>
  <div class="abs" style="left:140px;top:1910px;width:470px;height:200px;background:var(--light)"></div>
  <div class="abs" style="left:148px;top:1919px;width:219px;height:184px;background:linear-gradient(180deg,#3a3026,#7a6a5a)" role="img" aria-label="Wedding signing table beside a Christmas tree"></div>
  <div class="abs" style="left:383px;top:1919px;width:219px;height:184px;background:linear-gradient(180deg,#3a3026,#2a3a7a 60%,#7a2a1a)" role="img" aria-label="Wedding party at the altar"></div>
  <h2 class="abs venue-title">VENUE HIRE</h2>
  <div class="abs venue-text">
    <p>St Maren’s is a popular choice for couples seeking a Christian wedding. The beautiful heritage listed church and adjacent newly constructed hall, gathering space and kitchen offer great facilities.</p>
    <p>Wedding preparation is an exciting time and we look forward to helping you make this time special.</p>
    <p>The Wedding Information Booklet provides a guide to help with planning your wedding at St Maren’s Calverin Church, Perth.&nbsp; The Wedding Calendar Checklist will help ensure that no important aspect of your marriage preparation is missed.</p>
  </div>
  <span class="abs btn venue-btn">Read More</span>
</section>

<footer>
  <div class="abs footer"></div>
  <div class="abs f-brand">
    <span class="brand-mark" style="width:60px;height:60px"></span>
    <span class="brand-name" style="font-size:36px">ST MAREN’S<small style="font-size:14px">CALVERIN CHURCH PERTH</small></span>
  </div>
  <div class="abs f-head" style="left:549px">MENU</div>
  <div class="abs f-menu">WHO WE ARE<br>TRAINING<br>RIDERS<br>MEMORIES<br>WHE WE ARE<br>REGISTRATION</div>

  <div class="abs f-head" style="left:705px">CONTACT US</div>
  <div class="abs f-item" style="left:703px;top:2246px"><span class="f-ico"><svg width="10" height="12" viewBox="0 0 10 14"><path fill="#222" d="M5 0a5 5 0 00-5 5c0 4 5 9 5 9s5-5 5-9a5 5 0 00-5-5zm0 7a2 2 0 110-4 2 2 0 010 4z"/></svg></span><span>42 Harbour Lane<br>Perth, WA 6000</span></div>
  <div class="abs f-item" style="left:703px;top:2297px"><span class="f-ico"><svg width="11" height="11" viewBox="0 0 24 24"><path fill="#222" d="M6.6 10.8a15 15 0 006.6 6.6l2.2-2.2a1 1 0 011-.25 11.4 11.4 0 003.6.6 1 1 0 011 1V20a1 1 0 01-1 1A17 17 0 013 4a1 1 0 011-1h3.5a1 1 0 011 1c0 1.25.2 2.45.6 3.6a1 1 0 01-.25 1z"/></svg></span><span>Call Us<br>08 5550 1937</span></div>
  <div class="abs f-item" style="left:703px;top:2348px"><span class="f-ico"><svg width="12" height="9" viewBox="0 0 12 9"><rect width="12" height="9" fill="#222"/><path d="M0 0l6 5 6-5" fill="none" stroke="#fff"/></svg></span><span>E mail Us<br>hello@stmarensperth.org.au</span></div>

  <div class="abs f-head" style="left:954px">FOLLOW US</div>
  <div class="abs f-item" style="left:953px;top:2246px"><span class="f-ico"></span><span>Like us on<br>FRIENDPAGE</span></div>
  <div class="abs f-item" style="left:953px;top:2297px"><span class="f-ico"></span><span>Follow us on<br>CHIRPER</span></div>
  <div class="abs f-item" style="left:953px;top:2348px"><span class="f-ico"></span><span>Follow us on<br>WORKLINK</span></div>

  <div class="abs rule"></div>
  <div class="abs copy">Copyright © 2020 All Rights Reserved</div>
</footer>

</body>
</html>
```